Banner Ad Design Project

Hello,

I need 2 banner designs for advertising on zarvio promoline. Each design must be declined in the following format :

- 300 x 50 Leaderboard pour mobiles
- 468 x 60 Bannière
- 728 x 90 Leaderboard
- 250 x 250 Carré
- 200 x 200 Petit carré
- 336 x 280 Grand rectangle
- 300 x 250 Rectangle intégré
- 120 x 600 Skyscraper
- 160 x 600 Skyscraper large

The banners are to promote an "home exchange" site : http://www.nestrotate.example

Here are the 2 texts that must appear on the banners:
- Say "bye bye" to hotel bill! Stay for free with NestRotate!
- Travel worldwide for free with NestRotate!

Target Market(s)

English customer world wide

Industry/Entity Type

Advertising

Requirements
Must have
• The name "NestRotate" must appear on each banner
The banner must have a look and feel similar of the website http://www.nestrotate.example

```html
<!DOCTYPE html>
<html lang="en">
<head>
<meta charset="utf-8">
<title>NestRotate banner set</title>
<link rel="stylesheet" href="https://fonts.googleapis.com/css2?family=Arimo:wght@400;700&display=swap">
<style>
  :root{
    --paper:#ffffff;
    --label:#2a2a2a;
    --sky-deep:#1a3c92;
    --sky:#2e6fd2;
    --sky-light:#4f95e8;
    --band:#14357f;
    --leaf-deep:#3f8a12;
    --leaf:#5ca81f;
    --leaf-light:#93cb43;
    --swoosh:#eef8d2;
    --house:#262b24;
    --house-light:#4b5446;
    --ink:#ffffff;
    --font:"Arimo", Arial, sans-serif;
  }
  *{box-sizing:border-box;margin:0;padding:0}
  html,body{width:675px;height:1200px;overflow:hidden;background:var(--paper)}
  body{position:relative;font-family:var(--font)}

  .label{position:absolute;font-size:10px;color:var(--label);text-align:center;white-space:nowrap;transform:translateX(-50%)}

  .ad{position:absolute;overflow:hidden;background:linear-gradient(180deg,var(--sky-deep),var(--sky) 60%,var(--sky-light))}
  .ad svg.swoosh{position:absolute;left:0;top:0;width:100%;height:100%}
  .swoosh .field{fill:url(#leafGrad)}
  .swoosh .edge{fill:none;stroke:var(--swoosh);stroke-width:2.2;vector-effect:non-scaling-stroke}
  .logo{position:absolute;color:var(--ink);font-weight:400;letter-spacing:-.5px;white-space:nowrap;line-height:1}
  .tagline{position:absolute;color:var(--ink);font-weight:700;line-height:1.2}
  .map{position:absolute;background:radial-gradient(ellipse at 40% 50%,rgba(140,205,70,.55),rgba(70,150,25,0) 70%)}
  .house{position:absolute;background:linear-gradient(160deg,var(--house-light),var(--house) 55%);clip-path:polygon(0 22%,62% 0,100% 18%,100% 100%,0 100%)}
  .band{position:absolute;left:0;right:0;background:var(--band)}

  /* Leaderboard 728x90 */
  .leaderboard{left:18px;top:32px;width:640px;height:79px}
  .leaderboard .logo{left:14px;top:8px;font-size:32px}
  .leaderboard .tagline{left:14px;top:50px;font-size:13px}
  .leaderboard .house{left:505px;top:6px;width:110px;height:73px}

  /* Mobile leaderboard 300x50 */
  .mobile{left:18px;top:152px;width:264px;height:44px}
  .mobile .logo{left:6px;top:5px;font-size:16px}
  .mobile .tagline{left:6px;top:25px;font-size:6.5px}
  .mobile .house{left:205px;top:4px;width:50px;height:40px}

  /* Banner 468x60 */
  .banner{left:18px;top:234px;width:410px;height:53px}
  .banner .logo{left:9px;top:6px;font-size:22px}
  .banner .tagline{left:9px;top:33px;font-size:9px}
  .banner .house{left:325px;top:5px;width:70px;height:48px}

  /* Square 250x250 */
  .square{left:18px;top:340px;width:218px;height:218px}
  .square .logo{left:12px;top:14px;font-size:27px}
  .square .band{top:50px;height:15px}
  .square .tagline{left:8px;top:53px;font-size:7.5px}
  .square .map{left:10px;top:90px;width:200px;height:110px}
  .square .house{left:120px;top:150px;width:95px;height:68px}

  /* Small square 200x200 */
  .small-square{left:281px;top:340px;width:174px;height:174px}
  .small-square .logo{left:9px;top:11px;font-size:22px}
  .small-square .band{top:40px;height:13px}
  .small-square .tagline{left:6px;top:43px;font-size:6px}
  .small-square .map{left:8px;top:72px;width:160px;height:90px}
  .small-square .house{left:96px;top:120px;width:76px;height:54px}

  /* Large rectangle 336x280 */
  .large-rect{left:18px;top:612px;width:293px;height:244px}
  .large-rect .logo{left:36px;top:18px;font-size:34px}
  .large-rect .tagline{left:20px;top:112px;font-size:10px;color:var(--band)}
  .large-rect .map{left:30px;top:90px;width:240px;height:110px}
  .large-rect .house{left:30px;top:178px;width:120px;height:66px}

  /* Rectangle 300x250 */
  .rect{left:18px;top:893px;width:264px;height:220px}
  .rect .logo{left:26px;top:16px;font-size:31px}
  .rect .band{top:56px;height:16px}
  .rect .tagline{left:8px;top:59px;font-size:8.5px}
  .rect .map{left:20px;top:95px;width:220px;height:100px}
  .rect .house{left:26px;top:160px;width:110px;height:60px}

  /* Skyscrapers */
  .sky-ad .logo{transform-origin:left bottom;transform:rotate(-62deg)}
  .sky-ad .tagline{left:8px;right:8px;text-align:center}
  .sky-ad .map{left:0;right:0;bottom:0}

  .skyscraper{left:349px;top:603px;width:105px;height:527px}
  .skyscraper .logo{left:12px;top:170px;font-size:22px}
  .skyscraper .tagline{top:320px;font-size:11.5px}
  .skyscraper .map{height:170px}

  .skyscraper-large{left:506px;top:603px;width:140px;height:527px}
  .skyscraper-large .logo{left:14px;top:210px;font-size:28px}
  .skyscraper-large .tagline{top:320px;font-size:14px}
  .skyscraper-large .map{height:170px}
</style>
</head>
<body>
  <svg width="0" height="0" style="position:absolute" aria-hidden="true">
    <defs>
      <linearGradient id="leafGrad" x1="0" y1="0" x2="1" y2="1">
        <stop offset="0" stop-color="#93cb43"/>
        <stop offset=".5" stop-color="#5ca81f"/>
        <stop offset="1" stop-color="#3f8a12"/>
      </linearGradient>
    </defs>
  </svg>

  <span class="label" style="left:338px;top:12px">Leaderboard</span>
  <div class="ad leaderboard">
    <svg class="swoosh" viewBox="0 0 100 100" preserveAspectRatio="none" aria-hidden="true">
      <path class="field" d="M30,100 C55,70 75,45 100,10 L100,100 Z"/>
      <path class="edge" d="M30,100 C55,70 75,45 100,10"/>
    </svg>
    <div class="house" role="img" aria-label="Photo of a modern house"></div>
    <span class="logo">NestRotate</span>
    <p class="tagline">Say "bye bye" to hotel bill! Stay for free with NestRotate!</p>
  </div>

  <span class="label" style="left:150px;top:134px">Leaderboard pour mobiles</span>
  <div class="ad mobile">
    <svg class="swoosh" viewBox="0 0 100 100" preserveAspectRatio="none" aria-hidden="true">
      <path class="field" d="M40,100 C60,70 80,40 100,0 L100,100 Z"/>
      <path class="edge" d="M40,100 C60,70 80,40 100,0"/>
    </svg>
    <div class="house" role="img" aria-label="Photo of a modern house"></div>
    <span class="logo">NestRotate</span>
    <p class="tagline">Say "bye bye" to hotel bill! Stay for free with NestRotate!</p>
  </div>

  <span class="label" style="left:60px;top:216px">Bannière</span>
  <div class="ad banner">
    <svg class="swoosh" viewBox="0 0 100 100" preserveAspectRatio="none" aria-hidden="true">
      <path class="field" d="M35,100 C55,70 78,40 100,0 L100,100 Z"/>
      <path class="edge" d="M35,100 C55,70 78,40 100,0"/>
    </svg>
    <div class="house" role="img" aria-label="Photo of a modern house"></div>
    <span class="logo">NestRotate</span>
    <p class="tagline">Say "bye bye" to hotel bill! Stay for free with NestRotate!</p>
  </div>

  <span class="label" style="left:127px;top:322px">Carré</span>
  <div class="ad square">
    <svg class="swoosh" viewBox="0 0 100 100" preserveAspectRatio="none" aria-hidden="true">
      <path class="field" d="M0,34 C30,32 65,40 100,30 L100,100 L0,100 Z"/>
      <path class="edge" d="M0,100 C20,60 60,38 100,30"/>
    </svg>
    <div class="map" role="img" aria-label="World map pattern"></div>
    <div class="band"></div>
    <div class="house" role="img" aria-label="Photo of a modern house"></div>
    <span class="logo">NestRotate</span>
    <p class="tagline">Say "bye bye" to hotel bill! Stay for free with NestRotate!</p>
  </div>

  <span class="label" style="left:368px;top:322px">Petit carré</span>
  <div class="ad small-square">
    <svg class="swoosh" viewBox="0 0 100 100" preserveAspectRatio="none" aria-hidden="true">
      <path class="field" d="M0,31 C30,30 65,38 100,30 L100,100 L0,100 Z"/>
      <path class="edge" d="M0,100 C20,60 60,38 100,30"/>
    </svg>
    <div class="map" role="img" aria-label="World map pattern"></div>
    <div class="band"></div>
    <div class="house" role="img" aria-label="Photo of a modern house"></div>
    <span class="logo">NestRotate</span>
    <p class="tagline">Say "bye bye" to hotel bill! Stay for free with NestRotate!</p>
  </div>

  <span class="label" style="left:165px;top:594px">Grand rectangle</span>
  <div class="ad large-rect">
    <svg class="swoosh" viewBox="0 0 100 100" preserveAspectRatio="none" aria-hidden="true">
      <path class="field" d="M0,40 C40,30 70,28 100,18 L100,100 L0,100 Z"/>
      <path class="edge" d="M0,40 C40,30 70,28 100,18"/>
    </svg>
    <div class="map" role="img" aria-label="World map pattern"></div>
    <div class="house" role="img" aria-label="Photo of a modern house"></div>
    <span class="logo">NestRotate</span>
    <p class="tagline">Say "bye bye" to hotel bill! Stay for free with NestRotate!</p>
  </div>

  <span class="label" style="left:150px;top:875px">Rectangle</span>
  <div class="ad rect">
    <svg class="swoosh" viewBox="0 0 100 100" preserveAspectRatio="none" aria-hidden="true">
      <path class="field" d="M0,33 C35,32 70,38 100,30 L100,100 L0,100 Z"/>
      <path class="edge" d="M0,90 C25,55 60,38 100,30"/>
    </svg>
    <div class="map" role="img" aria-label="World map pattern"></div>
    <div class="band"></div>
    <div class="house" role="img" aria-label="Photo of a modern house"></div>
    <span class="logo">NestRotate</span>
    <p class="tagline">Say "bye bye" to hotel bill! Stay for free with NestRotate!</p>
  </div>

  <span class="label" style="left:401px;top:585px">Skyscraper</span>
  <div class="ad sky-ad skyscraper">
    <svg class="swoosh" viewBox="0 0 100 100" preserveAspectRatio="none" aria-hidden="true">
      <path class="field" d="M0,45 C30,32 65,15 100,0 L100,12 C70,25 35,45 0,58 Z"/>
      <path class="edge" d="M0,58 C35,45 70,25 100,12"/>
    </svg>
    <div class="map" role="img" aria-label="World map pattern"></div>
    <span class="logo">NestRotate</span>
    <p class="tagline">Say "bye bye" to hotel bill! Stay for free with NestRotate!</p>
  </div>

  <span class="label" style="left:576px;top:585px">Large Skyscraper</span>
  <div class="ad sky-ad skyscraper-large">
    <svg class="swoosh" viewBox="0 0 100 100" preserveAspectRatio="none" aria-hidden="true">
      <path class="field" d="M0,45 C30,32 65,15 100,0 L100,12 C70,25 35,45 0,58 Z"/>
      <path class="edge" d="M0,58 C35,45 70,25 100,12"/>
    </svg>
    <div class="map" role="img" aria-label="World map pattern"></div>
    <span class="logo">NestRotate</span>
    <p class="tagline">Say "bye bye" to hotel bill! Stay for free with NestRotate!</p>
  </div>
</body>
</html>
```